Landing Page Design

We need a landing page template designed to support a clients Zintro Bidlink Campaigns. The client is called Merrow Plumbing and they install and repair hot water systems (only). They provide no other plumbing services.

We are really looking for a great looking landing page that is both engaging and functional.

Target Market(s)

Residential/Domestic market. Typically wives and partners who are typically home or run the household.

Industry/Entity Type

Plumbing

Number of Pages Required

1 page

Requirements
Must have
• Strong branding
Strong call to actions
Great and obvious looking buttons
Nice to have
• Smart use of colour
Should not have
• The design should not use old-style, serif fonts.

Do not include any plumbing images

```html
<!DOCTYPE html>
<html lang="en">
<head>
<meta charset="utf-8">
<title>Merrow Plumbing – Hot Water Now</title>
<link href="https://fonts.googleapis.com/css2?family=Ubuntu:wght@400;500;700&family=Noto+Sans:wght@400;700&family=Roboto:wght@400&display=swap" rel="stylesheet">
<style>
:root{
  --cream:#fdf5d6;
  --cream-light:#fffbec;
  --orange:#f7931e;
  --orange-light:#ffa94a;
  --red:#d9220e;
  --red-dark:#a81405;
  --green-dark:#5a8a00;
  --lime:#c6d400;
  --olive:#6d8a0c;
  --yellow:#ffd800;
  --ink:#1e1e1e;
}
*{margin:0;padding:0;box-sizing:border-box}
html,body{width:1200px;height:1200px;overflow:hidden}
body{
  position:relative;
  background:radial-gradient(ellipse at 50% 110%, #f7e27c 0%, #fbeeb0 35%, var(--cream-light) 70%);
  font-family:"Roboto",sans-serif;color:var(--ink);
}
.abs{position:absolute}
.brand{left:137px;top:52px;width:220px;display:flex;align-items:flex-start;gap:12px}
.brand-dot{flex:none;width:28px;height:28px;margin-top:8px;border-radius:50%;background:var(--red)}
.brand-name{font-family:"Ubuntu",sans-serif;font-weight:700;font-size:36px;line-height:42px;color:var(--red)}
.top-banner{left:372px;top:20px;width:694px;height:86px;border:3px solid #fff;box-shadow:0 2px 5px rgba(0,0,0,.2);overflow:hidden;
  background:linear-gradient(90deg,#d8d8d8,#7e7e7e 40%,#c8c8c8)}
.top-banner svg{position:absolute;right:0;top:0}
.top-banner .tag{position:absolute;right:14px;top:8px;text-align:right;color:#fff;font-family:"Ubuntu",sans-serif;font-weight:500;font-size:20px;line-height:24px}
.call{left:636px;top:126px;display:flex;align-items:center;gap:12px;font-family:"Ubuntu",sans-serif;font-size:34px;color:var(--ink)}
.call b{font-weight:700}
.call i{font-style:italic;font-weight:400}
.panel{left:0;top:0}
.hero-photo{left:184px;top:258px;width:432px;height:275px;border:5px solid #fff;border-radius:3px;box-shadow:0 2px 6px rgba(0,0,0,.25);
  background:linear-gradient(90deg,#5e5e5e,#b3b3b3 45%,#efefef 75%,#fff)}
.hero-words{left:440px;top:330px;width:160px;text-align:right;font-family:"Ubuntu",sans-serif;line-height:64px}
.hero-words span{display:block;font-size:60px;color:#e8430c}
.hero-words span+span{color:var(--red-dark);font-size:50px}
.save-badge{left:192px;top:268px;width:90px;height:90px;border-radius:50%;background:var(--red);border:3px solid #fff;color:#fff;
  font-family:"Ubuntu",sans-serif;font-weight:700;text-align:center;font-size:20px;line-height:22px;padding-top:22px;transform:rotate(-10deg)}
.checks{left:648px;top:258px;list-style:none;font-family:"Noto Sans",sans-serif;font-size:27px;color:#fff;line-height:38.5px}
.checks li{display:flex;align-items:center;gap:12px}
.btn{top:469px;height:64px;border-radius:8px;display:flex;align-items:center;gap:10px;padding-left:14px;
  font-family:"Ubuntu",sans-serif;font-weight:500;font-size:20px;line-height:24px;box-shadow:0 3px 6px rgba(0,0,0,.2)}
.btn-quote{left:649px;width:186px;background:linear-gradient(#fff07a,var(--yellow) 50%,#f5b800);color:#3a2a00;text-align:center}
.btn-site{left:856px;width:160px;background:linear-gradient(#ff5a2a,var(--red) 50%,#c01000);color:#fff;text-align:center}
.card{left:135px;top:647px;width:925px;height:503px;background:#fff;border-radius:20px;box-shadow:0 -3px 6px rgba(0,0,0,.12);overflow:hidden}
.card-title{left:38px;top:40px;font-family:"Ubuntu",sans-serif;font-weight:500;font-size:27px;color:var(--green-dark)}
.card-photo{left:37px;top:106px;width:183px;height:188px;border:4px solid #fff;box-shadow:0 2px 5px rgba(0,0,0,.3);
  background:linear-gradient(135deg,#7a7a7a,#c7b8a8 60%,#e8ddd2)}
.card-copy{left:240px;top:105px;width:385px;font-size:15px;line-height:19.2px}
.card-copy p+p{margin-top:19px}
.offer{left:649px;top:0;width:276px;height:503px;background:linear-gradient(var(--lime),#a5b800 40%,var(--olive));padding:18px 22px}
.offer h2{font-family:"Ubuntu",sans-serif;font-weight:500;font-size:20px;line-height:25px;color:#fff;white-space:nowrap}
.keys{left:188px;top:112px;width:76px;height:30px;border-radius:15px;background:linear-gradient(90deg,#f5a623,#e8e8e8)}
.field{left:22px;width:235px;height:32px;background:#fff;font-family:"Roboto",sans-serif;font-size:15px;color:#333;padding:6px 10px}
.enquire{left:22px;top:441px;width:235px;height:36px;background:linear-gradient(#fff06a,var(--yellow));display:flex;align-items:center;
  font-family:"Ubuntu",sans-serif;font-weight:700;font-size:20px;color:#1a1a1a;padding-left:82px}
.ribbon{left:112px;top:1013px}
.ribbon-text{left:168px;top:1024px;font-family:"Ubuntu",sans-serif;font-weight:500;font-size:29px;color:#fff}
</style>
</head>
<body>

<div class="abs brand"><span class="brand-dot"></span><span class="brand-name">Merrow<br>Plumbing</span></div>

<div class="abs top-banner" role="img" aria-label="Banner photo of running hot water">
  <svg width="270" height="86" viewBox="0 0 270 86"><polygon points="0,0 270,0 270,86 220,86" fill="#e0360f"/><polygon points="0,0 20,0 230,86 220,86" fill="#e8b21a"/></svg>
  <div class="tag">HOT Water<br>Now!</div>
</div>

<div class="abs call">
  <svg width="42" height="42" viewBox="0 0 42 42"><circle cx="21" cy="21" r="20" fill="#4eb51f"/><circle cx="21" cy="21" r="14" fill="#2f8a0d"/><path d="M15 14 q-2 8 5 14 l3-3 -3-4 -2 1 q-2-3-1-5 l2-1 -1-4z" fill="#fff"/></svg>
  <span><b>Call NOW</b> on <i>9140 5382</i></span>
</div>

<svg class="abs panel" width="1200" height="700" viewBox="0 0 1200 700">
  <defs><linearGradient id="orangeFill" x1="0" y1="0" x2="0" y2="1"><stop offset="0" stop-color="#f7931e"/><stop offset=".5" stop-color="#ffab4d"/><stop offset="1" stop-color="#f7861a"/></linearGradient></defs>
  <polygon points="135,204 1062,206 1064,605 143,622" fill="#f28a1a"/>
  <polygon points="129,218 1056,188 1070,589 136,606" fill="url(#orangeFill)"/>
</svg>

<div class="abs hero-photo" role="img" aria-label="Photo of a rain shower head with falling water"></div>
<div class="abs hero-words"><span>HOT</span><span>water</span><span>now!</span></div>
<div class="abs save-badge">SAVE<br>$$$</div>

<ul class="abs checks">
  <li><svg width="32" height="28" viewBox="0 0 32 28"><path d="M2 15 l8-3 5 7 14-18 2 3 -15 23z" fill="#5cb81f"/></svg><span>Sydney <b>24</b> Hours <b>7</b> Days</span></li>
  <li><svg width="32" height="28" viewBox="0 0 32 28"><path d="M2 15 l8-3 5 7 14-18 2 3 -15 23z" fill="#5cb81f"/></svg><span>ON <b>TIME</b></span></li>
  <li><svg width="32" height="28" viewBox="0 0 32 28"><path d="M2 15 l8-3 5 7 14-18 2 3 -15 23z" fill="#5cb81f"/></svg><span><b>Professional</b> Technicians</span></li>
  <li><svg width="32" height="28" viewBox="0 0 32 28"><path d="M2 15 l8-3 5 7 14-18 2 3 -15 23z" fill="#5cb81f"/></svg><span>We Advise on <b>Rebates</b></span></li>
  <li><svg width="32" height="28" viewBox="0 0 32 28"><path d="M2 15 l8-3 5 7 14-18 2 3 -15 23z" fill="#5cb81f"/></svg><span><b>Authorised</b> Corva Dealer</span></li>
</ul>

<a class="abs btn btn-quote">
  <svg width="48" height="40" viewBox="0 0 48 40"><polygon points="4,18 30,4 44,10 40,24 14,38" fill="#39b6e8" stroke="#fff" stroke-width="2"/><circle cx="36" cy="12" r="3" fill="#fff"/></svg>
  <span>Book a<br>FREE Quote</span>
</a>
<a class="abs btn btn-site">
  <svg width="44" height="44" viewBox="0 0 44 44"><polygon points="22,4 42,22 36,22 36,40 8,40 8,22 2,22" fill="#fff"/><polygon points="22,4 42,22 38,24 22,10 6,24 2,22" fill="#2f6fd6"/><rect x="18" y="27" width="9" height="13" fill="#e46d1a"/></svg>
  <span>Visit our<br>WEBSITE</span>
</a>

<section class="abs card">
  <h1 class="abs card-title">Solar Hot Water System</h1>
  <div class="abs card-photo" role="img" aria-label="Photo of a woman enjoying a warm shower"></div>
  <div class="abs card-copy">
    <p>Lorem ipsum dolor sit amet, consectetur adipisicing elit, sed do eiusmod tempor incididunt ut labore et dolore magna aliqua. Ut enim ad minim veniam, quis nostrud exercitation ullamco laboris nisi ut aliquip ex ea commodo consequat. Duis aute irure dolor in reprehenderit in voluptate velit esse cillum dolore eu fugiat nulla pariatur.</p>
    <p>Excepteur sint occaecat cupidatat non proident, sunt in culpa qui officia deserunt mollit anim id est laborum. Lorem ipsum dolor sit amet, consectetur adipisicing elit.</p>
  </div>
  <aside class="abs offer">
    <h2>Take advantage of this<br>great offer. Contact Us<br>NOW on 9140 5382<br>or register your<br>interest below</h2>
    <div class="abs keys" role="img" aria-label="Illustration of a set of keys"></div>
    <div class="abs field" style="top:163px">First Name</div>
    <div class="abs field" style="top:201px">Surname</div>
    <div class="abs field" style="top:240px">Suburb</div>
    <div class="abs field" style="top:278px">Phone Number</div>
    <div class="abs field" style="top:318px">Email</div>
    <div class="abs field" style="top:356px;height:67px">Enquiry</div>
    <a class="abs enquire">
      <svg class="abs" style="left:16px;top:-4px" width="56" height="46" viewBox="0 0 56 46"><polygon points="4,14 40,2 52,32 16,44" fill="#f29a1f"/><polyline points="4,14 30,26 40,2" fill="none" stroke="#d9740c" stroke-width="2"/></svg>
      ENQUIRE NOW
    </a>
  </aside>
</section>

<svg class="abs ribbon" width="620" height="90" viewBox="0 0 620 90">
  <defs><linearGradient id="ribbonFill" x1="0" y1="0" x2="0" y2="1"><stop offset="0" stop-color="#e8430c"/><stop offset="1" stop-color="#c11205"/></linearGradient></defs>
  <polygon points="0,66 23,66 23,89" fill="#8c0c02"/>
  <polygon points="0,0 620,0 588,33 620,66 0,66" fill="url(#ribbonFill)"/>
</svg>
<div class="abs ribbon-text">Click here for information on Rebates</div>

</body>
</html>
```